Dr Lenora aesthetics - Grace Distilled

I need a logo design for a new aesthetics business in London. I am specialised in Botox, Dermal Fillers & Skin Pigmentation treatment. The slogan is Grace Distilled. I would like some of the writing on the card to be embossed. I would like a very elegant design with the following detail:

1. White and gray scale background. For the font colour try gold OR silver shades.
2. The business involves working on the face mostly. Anything that can be done with letter 'M'? Or any other logo?
3. The front of the card should have Dr Lenora Aesthetics and the slogan 'Grace Distilled'. The back should have my full name (Dr Lenora Brackwell), qualifications (MBBS MSC BSC), my website (www.ashfernclinicalcare.example), telephone number & email.
4. The back should also say treatments offered: ANTI-WRINKLE INJECTIONS. DERMAL FILLERS, LIP ENHANCEMENT, HYPERHYDROSIS. SKIN PIGMENTATION

Thank you very much
Updates

Project Deadline Extended
Reason: Delays in market research response. I would be grateful for an extension please. Many thanks

Target Market(s)

Female and male aged 18 and above

Industry/Entity Type

Business

Contact Information for Business Card

Elegant design. Square corners. British standard size. Horizontal design. Should contain the slogan, contact details.

Font styles to use
Script

Colors
c9c9c9
fbed22
ffffff
f5f5f5
000000

Requirements
Must have
• All that's mentioned above
Nice to have
• A logo with the outline of a female face. Or anything that can be done with the letter M of Lenora.
Should not have
• No colours like green / purple / orange

```html
<!DOCTYPE html>
<html lang="en">
<head>
<meta charset="utf-8">
<title>Dr Lenora Aesthetics – Business Card</title>
<link rel="stylesheet" href="https://fonts.googleapis.com/css2?family=Didact+Gothic&family=Parisienne&display=swap">
<style>
  :root {
    --backdrop: #d9d9d9;
    --card: #ffffff;
    --card-edge: #ececec;
    --gold: #a88426;
    --gold-soft: #c2a04a;
    --ink-shadow: rgba(0,0,0,0.18);
  }
  * { margin: 0; padding: 0; box-sizing: border-box; }
  html, body {
    width: 1200px; height: 964px; overflow: hidden;
    background: var(--backdrop);
  }
  .canvas { position: relative; width: 1200px; height: 964px; }

  .card {
    position: absolute;
    width: 650px; height: 420px;
    background: var(--card);
    border: 1px solid var(--card-edge);
    box-shadow: 0 10px 28px var(--ink-shadow);
    color: var(--gold);
    font-family: "Didact Gothic", "Century Gothic", sans-serif;
  }
  .card--back { left: 180px; top: 40px; }
  .card--front { left: 370px; top: 504px; }

  /* Back side */
  .holder { text-align: center; padding-top: 40px; }
  .holder__name { font-size: 34px; letter-spacing: 0.5px; }
  .holder__quals { font-size: 14px; letter-spacing: 2px; margin-top: 4px; }

  .contact { text-align: center; margin-top: 26px; font-size: 17px; line-height: 1.7; }
  .contact__row { display: flex; justify-content: center; gap: 34px; }
  .contact__item { display: inline-flex; align-items: center; gap: 8px; }
  .contact__icon { width: 18px; height: 18px; fill: var(--gold); }

  .treatments {
    display: grid; grid-template-columns: 1fr 1fr;
    column-gap: 30px; padding: 34px 60px 0 70px;
    list-style: none; font-size: 16px; letter-spacing: 0.4px;
  }
  .treatments li { display: flex; align-items: center; gap: 10px; margin-bottom: 12px; }
  .tick { width: 20px; height: 18px; flex: none; }
  .tick rect { fill: none; stroke: var(--gold); stroke-width: 1.4; }
  .tick path { fill: none; stroke: var(--gold); stroke-width: 2.4; stroke-linecap: round; stroke-linejoin: round; }

  /* Front side */
  .brand {
    position: absolute; inset: 0;
    display: flex; flex-direction: column; align-items: center; justify-content: center;
  }
  .brand__mark { width: 92px; height: 92px; border-radius: 50%; background: var(--gold-soft); margin-bottom: 14px; }
  .brand__name { font-family: "Parisienne", cursive; font-size: 52px; line-height: 1.1; }
  .brand__slogan { font-size: 26px; letter-spacing: 6px; margin-top: 10px; }
</style>
</head>
<body>
<main class="canvas">

  <section class="card card--back" aria-label="Card back">
    <header class="holder">
      <h1 class="holder__name">Dr Lenora Brackwell</h1>
      <p class="holder__quals">MBBS MSC BSC</p>
    </header>

    <div class="contact">
      <div class="contact__row">
        <span class="contact__item">
          <svg class="contact__icon" viewBox="0 0 24 24" aria-hidden="true"><path d="M3 8c0-2 3-4 9-4s9 2 9 4v2h-5V8H8v2H3zM6 12h12l2 8H4z"/></svg>
          +44 7700 900123
        </span>
        <span class="contact__item">
          <svg class="contact__icon" viewBox="0 0 24 24" aria-hidden="true"><path d="M2 5h20v14H2zM4 7v1l8 5 8-5V7z"/></svg>
          drlenoraaesthetics@mail.example
        </span>
      </div>
      <div>www.ashfernclinicalcare.example</div>
    </div>

    <ul class="treatments">
      <li><svg class="tick" viewBox="0 0 20 18" aria-hidden="true"><rect x="1" y="5" width="12" height="12"/><path d="M3 10l4 5L18 2"/></svg>ANTI-WRINKLE INJECTIONS</li>
      <li><svg class="tick" viewBox="0 0 20 18" aria-hidden="true"><rect x="1" y="5" width="12" height="12"/><path d="M3 10l4 5L18 2"/></svg>LIP ENHANCEMENT</li>
      <li><svg class="tick" viewBox="0 0 20 18" aria-hidden="true"><rect x="1" y="5" width="12" height="12"/><path d="M3 10l4 5L18 2"/></svg>DERMAL FILLERS</li>
      <li><svg class="tick" viewBox="0 0 20 18" aria-hidden="true"><rect x="1" y="5" width="12" height="12"/><path d="M3 10l4 5L18 2"/></svg>HYPERHYDROSIS</li>
      <li><svg class="tick" viewBox="0 0 20 18" aria-hidden="true"><rect x="1" y="5" width="12" height="12"/><path d="M3 10l4 5L18 2"/></svg>SKIN PIGMENTATION</li>
    </ul>
  </section>

  <section class="card card--front" aria-label="Card front">
    <div class="brand">
      <span class="brand__mark" aria-hidden="true"></span>
      <p class="brand__name">Dr. Lenora Aesthetics</p>
      <p class="brand__slogan">Grace Distilled</p>
    </div>
  </section>

</main>
</body>
</html>
```